Fancy looking Inspection Postcard

Postcard needed for customers to inspect their product once it is delivered. We'll be giving them the steps for inspecting their product and to contact us if any issues arise. Would like to see something that sticks out but uses our company's colors. Would like to see creativity. Possibly utilizing the diamond steel background like we have in our logo.

Target Market(s)

Customers of our manufacturing shop

Industry/Entity Type

Manufacturing - metal wall art, custom products

Requirements
Must have
• our colors and logo
Nice to have
• get creative. i like creativity

```html
<!DOCTYPE html>
<html lang="en">
<head>
<meta charset="utf-8">
<title>Ridgeline Metalworks – Inspection Postcard</title>
<link rel="stylesheet" href="https://fonts.googleapis.com/css2?family=League+Gothic&family=Montserrat:wght@300;400;700&display=swap">
<style>
  :root {
    --page-bg: #231f20;
    --card-bg: #0b0b0b;
    --plate-tone: #1a1a1a;
    --brand-yellow: #fff200;
    --brand-green: #74a947;
    --copy-white: #ffffff;
  }
  * { margin: 0; padding: 0; box-sizing: border-box; }
  html, body {
    width: 1200px; height: 1200px; overflow: hidden;
    background: var(--page-bg);
  }
  .postcard {
    position: absolute; left: 150px; top: 300px;
    width: 899px; height: 600px;
    background: var(--card-bg);
    overflow: hidden;
  }
  .plate-texture {
    position: absolute; inset: 0 0 12px 0;
    background:
      radial-gradient(ellipse at 55% 45%, var(--plate-tone) 0%, var(--card-bg) 75%);
  }
  .accent-band {
    position: absolute; left: 0; right: 0; bottom: 0; height: 12px;
    background: var(--brand-yellow);
  }
  .brand-name {
    position: absolute; left: 35px; top: 70px; width: 153px;
    font-family: "League Gothic", sans-serif;
    font-size: 54px; line-height: 50px;
    color: var(--brand-green);
    text-align: center;
    letter-spacing: 1px;
  }
  .contact {
    position: absolute; left: 35px; top: 256px; width: 260px;
    font-family: "Montserrat", sans-serif;
    font-size: 14.5px; line-height: 18px;
    color: var(--brand-green);
    font-weight: 300;
  }
  .contact p { margin-bottom: 11px; }
  .contact .value {
    display: block; color: var(--brand-yellow); font-weight: 700;
    letter-spacing: -0.3px;
  }
  .contact .value-inline { color: var(--brand-yellow); font-weight: 700; letter-spacing: -0.3px; }
  .contact .heading {
    font-weight: 700; color: var(--brand-green); margin-top: 14px; margin-bottom: 4px;
    letter-spacing: -0.3px;
  }
  .contact .review { line-height: 24px; margin-bottom: 10px; }
  .review-site { color: var(--brand-yellow); font-weight: 700; font-size: 19px; }
  .steps-art { position: absolute; left: 0; top: 0; }
  .step-label {
    font-family: "Montserrat", sans-serif; font-weight: 700;
    font-size: 31px; fill: var(--brand-yellow);
  }
  .step-number {
    font-family: "League Gothic", sans-serif; font-size: 170px;
    fill: none; stroke: var(--brand-green); stroke-width: 2.4;
  }
  .step-ring { fill: none; stroke: var(--brand-yellow); stroke-width: 1.6; }
  .step-copy {
    position: absolute;
    font-family: "League Gothic", sans-serif;
    font-size: 22px; line-height: 19px;
    color: var(--copy-white);
    letter-spacing: 0.2px;
  }
  .step-copy p + p { margin-top: 6px; }
  .step-one   { left: 350px; top: 123px; }
  .step-one p + p { margin-top: 6px; }
  .step-two   { left: 676px; top: 122px; }
  .step-three { left: 366px; top: 384px; }
  .step-four  { left: 676px; top: 384px; }
</style>
</head>
<body>
  <main class="postcard">
    <div class="plate-texture" role="img" aria-label="Diamond steel plate texture background"></div>

    <div class="brand-name">RIDGELINE METALWORKS</div>

    <section class="contact">
      <p>Email us at <span class="value">orders@ridgelinemetal.com</span></p>
      <p>Shoot us a text <span class="value">(555) 204 0193</span></p>
      <p>or reach out at via <span class="value">www.ridgelinemetal.com/contact</span></p>
      <p class="heading">DID WE DO A GOOD JOB?</p>
      <p class="review">If you think so leave us a<br>review on <span class="review-site">Reviewly</span></p>
      <p>If not, please let us know <span class="value">info@ridgelinemetal.com</span></p>
      <p>or call us <span class="value-inline">555 476 0127</span></p>
    </section>

    <svg class="steps-art" width="899" height="588" viewBox="0 0 899 588" aria-hidden="true">
      <path class="step-ring" d="M338 88 A110 110 0 1 1 331 223"/>
      <path class="step-ring" d="M643 88 A110 110 0 1 1 636 223"/>
      <path class="step-ring" d="M338 367 A110 110 0 1 1 331 502"/>
      <path class="step-ring" d="M643 367 A110 110 0 1 1 636 502"/>

      <text class="step-label" transform="translate(302 220) rotate(-90)">STEP</text>
      <text class="step-label" transform="translate(597 220) rotate(-90)">STEP</text>
      <text class="step-label" transform="translate(288 499) rotate(-90)">STEP</text>
      <text class="step-label" transform="translate(593 499) rotate(-90)">STEP</text>

      <text class="step-number" x="292" y="220">1</text>
      <text class="step-number" x="601" y="220">2</text>
      <text class="step-number" x="292" y="500">3</text>
      <text class="step-number" x="598" y="500">4</text>
    </svg>

    <div class="step-copy step-one">
      <p>INSPECT GENERAL SHAPE</p>
      <p>IS IT WHAT YOU EXPECTED ?</p>
      <p>IS IT BENT, DISORIENTED ?</p>
    </div>
    <div class="step-copy step-two">
      <p>INSPECT THE WELDS IF<br>THERE ARE ANY</p>
      <p>DO THEY LOOK CLEAN?</p>
      <p>ARE THERE ANY GAPS?</p>
    </div>
    <div class="step-copy step-three">
      <p>INSPECT THE FINISH</p>
      <p>ARE THERE ANY AREAS<br>NOT FINISHED?</p>
      <p>ARE THE COLORS WHAT<br>YOU EXPECTED?</p>
    </div>
    <div class="step-copy step-four">
      <p>CHECK FOR<br>FUNCTIONALITY</p>
      <p>DOES IT WORK THE WAY<br>YOU WANT IT TO</p>
      <p>IS IT WHAT YOU<br>EXPECTED ?</p>
    </div>

    <div class="accent-band"></div>
  </main>
</body>
</html>
```